Dental clinic brochure design (Z fold)

We need a new brochure design made for our dental clinic - Brindlemoor Dental Surgery. One side is in English, the other is in Vietnamese - all text and translations provided in brochure sample with further instructions in word doc. We require a brochure design in a Z fold to convey a family friendly dental clinic, incorporating our logo colour into the theme and designers choice on complimentary colours. Additional high quality images are provided for use if required or free to use own images.

Colors
33b8a4
00a990
86cfc6

Requirements
Must have
• Easy to read font, flows from text to pictures and page to page
• At least 2 dental images

```html
<!DOCTYPE html>
<html lang="en">
<head>
<meta charset="utf-8">
<title>Brindlemoor Dental Surgery – Brochure Panel</title>
<link rel="stylesheet" href="https://fonts.googleapis.com/css2?family=Cinzel:wght@400;700;900&family=Playfair+Display:ital,wght@0,400;0,700;1,700;1,900&display=swap">
<style>
  :root {
    --teal: #33b8a4;
    --teal-deep: #00a990;
    --teal-soft: #86cfc6;
    --slate: #666666;
    --ink: #5a5a5a;
    --paper: #ffffff;
  }
  * { margin: 0; padding: 0; box-sizing: border-box; }
  html, body { width: 1200px; height: 716px; overflow: hidden; background: var(--paper); }
  .brochure { position: relative; width: 1200px; height: 716px; font-family: "Playfair Display", Georgia, serif; color: var(--ink); }

  .col { position: absolute; text-align: center; }
  .col-benefits { left: 90px; width: 260px; }
  .col-promos { left: 395px; width: 250px; }

  .heading-main { font-family: "Cinzel", serif; font-weight: 900; color: var(--teal); line-height: 1; }
  .benefits-title { top: 70px; font-size: 32px; letter-spacing: 0.5px; }
  .benefits-sub { font-family: "Cinzel", serif; font-weight: 400; font-size: 19px; letter-spacing: 5px; color: var(--ink); margin-top: 5px; }
  .promos-title { top: 68px; font-size: 32px; line-height: 0.95; letter-spacing: 0.5px; }

  .body-copy { font-size: 19px; line-height: 24.5px; color: var(--ink); }
  .benefits-copy { top: 170px; }
  .eligibility { top: 332px; font-weight: 700; font-size: 22px; line-height: 27.5px; letter-spacing: 1.5px; }
  .phone-callout { top: 415px; font-style: italic; font-weight: 900; font-size: 29px; color: var(--teal); letter-spacing: 0.5px; }

  .promo-checkup { top: 170px; }
  .promo-whitening { top: 257px; }
  .promo-ortho { top: 362px; }
  .promo-note { top: 430px; font-style: italic; font-weight: 700; font-size: 17px; line-height: 21px; color: var(--teal); }

  .team-banner { position: absolute; left: 670px; top: 68px; width: 313px; height: 64px; background: var(--slate); color: #fff; text-align: center; font-family: "Cinzel", serif; font-weight: 400; font-size: 21px; line-height: 24px; letter-spacing: 4px; padding-top: 9px; }
  .team-list { position: absolute; left: 670px; top: 171px; width: 313px; text-align: center; list-style: none; color: var(--teal); font-size: 13.5px; line-height: 16.5px; }
  .team-list li { margin-bottom: 15.5px; }

  .location-map { position: absolute; left: 728px; top: 317px; width: 208px; height: 237px; background: linear-gradient(160deg, #f4f4f4, #e4e4e4); }

  .kids-photo { position: absolute; left: 60px; top: 520px; width: 610px; height: 196px; background: linear-gradient(90deg, #d9c6a8 0%, #c98f64 25%, #e3a7b8 45%, #f2d35a 65%, #c4d9e6 82%, #e4553a 100%); }

  .contact-panel { position: absolute; left: 670px; top: 559px; width: 313px; height: 157px; background: var(--slate); color: #fff; text-align: right; padding: 25px 47px 0 0; font-style: normal; font-size: 15.5px; line-height: 19.5px; font-weight: 700; }
  .contact-panel .contact-phone { margin-top: 19px; }
</style>
</head>
<body>
<main class="brochure">

  <section class="col col-benefits heading-main benefits-title">
    Child Dental
    <div class="benefits-sub">Benefits Scheme</div>
  </section>
  <p class="col col-benefits body-copy benefits-copy">A dental benefits program is available for eligible children aged 2 to 17 and will receive $1000 for dental treatments.</p>
  <p class="col col-benefits body-copy eligibility">To check if your children are eligible call us on</p>
  <p class="col col-benefits phone-callout">9460 2184</p>

  <h2 class="col col-promos heading-main promos-title">Special<br>Promotions</h2>
  <p class="col col-promos body-copy promo-checkup">Gap free dental check-up, clean &amp; x-rays for all health insurances**</p>
  <p class="col col-promos body-copy promo-whitening">At home whitening kit now $199 limited time only (normally $395)</p>
  <p class="col col-promos body-copy promo-ortho">Braces, dentures and implants are available at our</p>
  <p class="col col-promos promo-note">**Conditions apply—Ask staff for more information</p>

  <h2 class="team-banner">Our<br>Expert Team</h2>
  <ul class="team-list">
    <li>Dr Mai Tran BDSc (Melb), ICCDE</li>
    <li>Dr Quan Vo BDSc (Melb), FICCDE FRACDS,<br>PGradDipCD Implants (Melb)</li>
    <li>Dr Linh Nguyen BHsc Mdent (Latrobe)</li>
    <li>Dr Kate Bui BDS (Adl)</li>
  </ul>

  <div class="location-map" role="img" aria-label="Street map showing the clinic location near the library, station and main roads"></div>

  <div class="kids-photo" role="img" aria-label="Photo of a group of smiling children"></div>

  <address class="contact-panel">
    48 Ashcombe Road<br>Kelverton, VIC 3187
    <div class="contact-phone">(03) 9460 2184</div>
    admin@brindlemoordental.com.au
  </address>

</main>
</body>
</html>
```